nutrition company business card

I would like to have a business card that has two sides, one being the green color from the Company name on the logo. I am open to ideas and looks that work with my logo. I like the idea of having a negative image of the tree on the green side.

For my information on the card I must have:
Linda Moorcombe
415-872-6041
lindamoorcombe@quellmail.net

This area will need to be updated once I complete my schooling.

Reason: I need to extend my deadline by one day as I have been sick the last week and not had time to review all the new designs. Thank you.

Industry/Entity Type

Nutrition

Requirements
Must have
• I would like to have a business card that has two sides, one being the green color from the Company name on the logo. I am open to ideas and looks that work with my logo. I like the idea of having a negative image of the tree on the green side.
• For my information on the card I must have:
• Linda Moorcombe
• 415-872-6041
• lindamoorcombe@quellmail.net
• This area will need to be updated once I complete my schooling.

```html
<!DOCTYPE html>
<html lang="en">
<head>
<meta charset="utf-8">
<title>Rooted Table — Business Card</title>
<link rel="stylesheet" href="https://fonts.googleapis.com/css2?family=Quicksand:wght@500;600&family=Ubuntu:wght@400&display=swap">
<style>
  :root {
    --leaf-green: #8bc143;
    --bark-grey: #948a83;
    --card-white: #ffffff;
    --backdrop: #ece8e3;
  }
  * { box-sizing: border-box; margin: 0; padding: 0; }
  html, body { width: 1200px; height: 1000px; overflow: hidden; }
  body { background: var(--backdrop); position: relative; font-family: "Quicksand", sans-serif; }

  .card {
    position: absolute;
    width: 500px;
    height: 300px;
    box-shadow: 0 4px 14px rgba(0,0,0,0.12);
    overflow: hidden;
  }

  /* Back side */
  .card--back { left: 350px; top: 130px; background: var(--leaf-green); }
  .back-mark {
    position: absolute; left: 50%; top: 50%;
    width: 146px; height: 146px; margin: -73px 0 0 -73px;
    border: 4px solid var(--bark-grey); border-radius: 50%;
    display: flex; align-items: center; justify-content: center;
  }
  .back-mark__name {
    color: var(--card-white); font-weight: 600; font-size: 19px;
    text-align: center; line-height: 1.15;
  }

  /* Front side */
  .card--front { left: 350px; top: 520px; background: var(--card-white); }
  .brand {
    position: absolute; left: 0; right: 0; top: 34px;
    display: flex; flex-direction: column; align-items: center;
  }
  .brand__circle {
    width: 64px; height: 64px; border: 3px solid var(--bark-grey); border-radius: 50%;
  }
  .brand__name {
    margin-top: 14px; color: var(--leaf-green); font-weight: 500; font-size: 27px; letter-spacing: 0.3px;
  }
  .rule {
    position: absolute; left: 0; right: 0; top: 194px; height: 3px; background: var(--bark-grey);
  }
  .contact-band {
    position: absolute; left: 0; right: 0; top: 203px; bottom: 0; background: var(--leaf-green);
    color: var(--card-white); font-family: "Ubuntu", sans-serif;
  }
  .contact-band__name {
    position: absolute; left: 44px; top: 38px; font-size: 19px; letter-spacing: 0.4px;
  }
  .contact-band__divider {
    position: absolute; left: 246px; top: 22px; width: 2px; height: 52px; background: var(--card-white);
  }
  .contact-band__details {
    position: absolute; left: 262px; top: 26px; font-size: 14px; line-height: 22px; letter-spacing: 0.3px;
  }
</style>
</head>
<body>
  <section class="card card--back" aria-label="Business card, back">
    <div class="back-mark">
      <span class="back-mark__name">Rooted<br>Table</span>
    </div>
  </section>

  <section class="card card--front" aria-label="Business card, front">
    <div class="brand">
      <div class="brand__circle"></div>
      <div class="brand__name">Rooted Table</div>
    </div>
    <div class="rule"></div>
    <div class="contact-band">
      <div class="contact-band__name">Linda Moorcombe</div>
      <div class="contact-band__divider"></div>
      <div class="contact-band__details">
        <div>415-872-6041</div>
        <div>lindamoorcombe@quellmail.net</div>
      </div>
    </div>
  </section>
</body>
</html>
```